We Buy Houses Website

Looking for a highly motivated and skillfull designer to design and code me a "we Buy Houses" type website. I have a potential logo, but if you think you can make a BETTER one, please do try and incorporate it in your template. I am looking for creativity, professionalism, simple yet elegant. I will need a simple form on the front of the template along with pictures I provide you of recent houses I have bought. Look at these sites for examples of the layout of the website:

http://www.brickwaleholdings.example/
http://www.marlowtakesplots.example/
http://www.quickdwellingexit.example/

If you make me a design that blows me away, and you are dependable, you will become part of my team and in charge of the web aspect which will include designing, updating, any and all graphics and logo work, SEO, coding. If you have skills in all of these areas please make me a design and lets do business!! The name of the website will be "Tovin Takes Homes" at TovinTakesHomes.example

I have uploaded some pictures of houses that we have done, please feel free to incorporate this into the banner or the design, etc. I want them to know we buy houses in ANY condition, as is, cash, can close immediately so they can get on with their life. We have many options to help them find a solution to whatever problem they have. We are in the business of helping people.

Target Market(s)

People looking to sell their houses
people facing foreclosure, bankruptcy, death in the family, divorce, anyone that we can help
people with ugly houses that need a lot of repair

Industry/Entity Type

Business

Font styles to use
Serif
Sans Serif

Colors

Designer to choose colors to be used in the design.

Requirements
Must have
• must have a simple form on the front of the page, preferrably near the banner, with the few required fields to help someone get started putting in their interest to sell their house, view the 2 websites i put as examples to see what kind of fields it should have.

My phone number (555) 481-7720 along with a Tovin Takes Homes logo, clean simple and elegant and professional. I want a nice color scheme that is not white but professional and has a wow factor.

```html
<!DOCTYPE html>
<html lang="en">
<head>
<meta charset="utf-8">
<title>Tovin Takes Homes — We Buy Houses Philadelphia</title>
<link rel="stylesheet" href="https://fonts.googleapis.com/css2?family=Source+Sans+3:wght@400;600;700&display=swap">
<style>
:root{
  --navy:#050b20;
  --lime:#a7d81c;
  --lime-dark:#7fae08;
  --page:#e7e7e7;
  --panel:#ffffff;
  --ink:#1b1f2a;
  --muted:#6a6d72;
  --field-line:#c9c9c9;
  --footer:#232323;
  --footer-text:#d8d8d8;
}
*{box-sizing:border-box;margin:0;padding:0}
html,body{width:1200px;height:2170px;overflow:hidden}
body{position:relative;background:var(--page);font-family:"Source Sans 3",Arial,sans-serif;color:var(--ink)}
.abs{position:absolute}

/* header */
.site-header{left:0;top:0;width:1200px;height:187px;background:var(--navy)}
.brand{left:74px;top:62px;display:flex;align-items:center;gap:14px}
.brand-mark{width:44px;height:44px;background:var(--lime)}
.brand-name{font-size:30px;font-weight:700;color:var(--lime);letter-spacing:.5px}
.call-label{right:110px;top:48px;color:#fff;font-size:18px}
.call-number{right:110px;top:70px;color:var(--lime);font-size:22px}
.call-icon{left:1098px;top:54px}
.main-nav{top:128px;color:#fff;font-size:18px}

/* slider */
.slider-frame{left:73px;top:217px;width:727px;height:449px;background:#fff;box-shadow:0 14px 22px rgba(0,0,0,.28)}
.slider-photo{left:83px;top:226px;width:709px;height:432px;background:linear-gradient(180deg,#2d5fd8 0%,#5a86e4 45%,#8b857a 62%,#5c564d 100%)}
.slide-title{left:106px;top:572px;color:#fff;font-size:27px;font-weight:600}
.slide-text{left:106px;top:614px;color:#fff;font-size:20px}
.slider-arrow{top:412px;width:30px;height:32px;background:#f3f3f3;display:flex;align-items:center;justify-content:center}

/* form */
.lead-form{left:800px;top:233px;width:324px;height:420px;background:#f7f7f7}
.lead-form-head{height:61px;background:var(--navy);color:#fff;font-size:27px;display:flex;align-items:center;justify-content:center}
.field{left:27px;width:271px;height:36px;background:#fff;border:1px solid var(--field-line);font-size:13px;color:#666;padding:9px 12px}
.field-area{height:63px}
.submit-btn{left:198px;top:365px;width:98px;height:35px;background:linear-gradient(180deg,#c3ef3a,var(--lime-dark));color:var(--navy);font-size:16px;font-weight:700;display:flex;align-items:center;justify-content:center;border:1px solid #86b20f}

/* content */
.content-panel{left:73px;top:707px;width:1053px;height:1359px;background:var(--panel);box-shadow:0 0 6px rgba(0,0,0,.12)}
.section-title{left:93px;font-size:34px;font-weight:400;color:var(--ink)}
.body-copy{left:93px;width:1010px;font-size:11px;line-height:21px;color:var(--muted)}
.map-area{left:91px;top:945px;width:446px;height:275px;background:var(--lime);border-radius:40px 80px 60px 120px}
.pitch{left:585px;top:944px;width:515px;font-size:22px;line-height:36px;color:var(--ink);white-space:nowrap}
.benefit-list{left:585px;top:1032px;list-style:none;font-size:12.5px;color:var(--ink)}
.benefit-list li{height:29.8px;display:flex;align-items:center;gap:14px}
.reason{font-size:14px;color:#444;display:flex;align-items:center;gap:12px}
.step{left:98px;display:flex;align-items:center;gap:16px;font-size:14.5px;color:#444}
.step-num{width:27px;height:27px;border-radius:50%;background:radial-gradient(circle at 40% 35%,#c9f046,var(--lime-dark));color:var(--navy);font-size:14px;font-weight:700;display:flex;align-items:center;justify-content:center}

/* footer */
.site-footer{left:0;top:2070px;width:1200px;height:100px;background:var(--footer)}
.footer-links{left:102px;top:2094px;color:var(--footer-text);font-size:12.5px}
.copyright{left:102px;top:2124px;color:var(--footer-text);font-size:12.5px}
.social{top:2108px;width:28px;height:28px}
</style>
</head>
<body>

<header class="abs site-header"></header>
<div class="abs brand"><span class="brand-mark"></span><span class="brand-name">Tovin Takes Homes</span></div>
<div class="abs call-label">Call today</div>
<div class="abs call-number">+61 02 5550 1942</div>
<svg class="abs call-icon" width="24" height="34" viewBox="0 0 24 34" aria-hidden="true"><path d="M6 2 L11 8 L8 12 Q10 20 15 24 L19 21 L23 27 L18 32 Q2 26 2 6 Z" fill="none" stroke="#a7d81c" stroke-width="3" stroke-linejoin="round"/></svg>
<nav>
  <div class="abs main-nav" style="left:655px">Home</div>
  <div class="abs main-nav" style="left:744px">Our Projects</div>
  <div class="abs main-nav" style="left:881px">We Buy Houses</div>
  <div class="abs main-nav" style="left:1041px">Contact Us</div>
</nav>

<div class="abs slider-frame"></div>
<div class="abs slider-photo" role="img" aria-label="Photo of a recently bought single-storey house with a garage under blue sky"></div>
<div class="abs slide-title">Eodem modo typin qui nunc nobis videntur</div>
<div class="abs slide-text">Typi non habent claritatem insitam; est usus legentis in iis qui facit</div>
<div class="abs slider-arrow" style="left:83px"><svg width="8" height="10"><path d="M7 0 L0 5 L7 10Z" fill="#222"/></svg></div>
<div class="abs slider-arrow" style="left:762px"><svg width="8" height="10"><path d="M1 0 L8 5 L1 10Z" fill="#222"/></svg></div>

<form class="abs lead-form">
  <div class="lead-form-head">Sell us your house</div>
  <div class="abs field" style="top:84px">Name</div>
  <div class="abs field" style="top:134px">Email</div>
  <div class="abs field" style="top:184px">Phone Number</div>
  <div class="abs field" style="top:235px">Property Address</div>
  <div class="abs field field-area" style="top:286px">Describe the condition of the property</div>
  <div class="abs submit-btn">SUBMIT</div>
</form>

<main class="abs content-panel"></main>

<h1 class="abs section-title" style="top:747px">We Buy Houses Philadelphia</h1>
<p class="abs body-copy" style="top:812px">Before we can do one of the beautiful renovations featured here on our site we first have to buy hous-es. "I need to sell my house" is one thing that we've been hearinhere in Philadelphia since 2008. Orrick Lane Properties buys houses for cash and we'll buy your house too, no matter what condition it is in. Our Philadelphia area home buying company is Delvane Home Buyers.<br>Delvane Home Buyers likes to work with homeowners who want to Sell their Home Quickly, in As-Is condition, and get a Cash buyout or don't want the hassles of listing with a Realtor and waiting for a sale. We Buy Houses, Rowhomes, Duplexes, Triplexes, Quads, Condos, Land and Commercial Buildings in PHILADELPHIA and the surrounding area.</p>

<div class="abs map-area" role="img" aria-label="Map of the United States showing the service area"></div>
<div class="abs pitch">Are you are saying to yourself &nbsp;“I need to sell my house?”<br>We are home buyers who will pay cash and buy it fast!</div>
<ul class="abs benefit-list">
  <li><span>→</span>We Pay Cash</li>
  <li><span>→</span>We Buy Houses As-Is</li>
  <li><span>→</span>We Pay Closing Costs</li>
  <li><span>→</span>We Act Fast so you can move on</li>
  <li><span>→</span>We Don't Ask You to do Any Repairs</li>
  <li><span>→</span>Serving all of Philadelphia &amp; the Surrounding Counties</li>
</ul>

<h2 class="abs section-title" style="top:1288px">If You Need To Sell Fast Sell to Us</h2>
<p class="abs body-copy" style="top:1358px">We buy houses for all sorts of reasons and will make you a hassle-free cash offer for your house in Philadelphia. It doesn't matter what the situation is, structural defects or if its a fixer-upper, that's o.k. with us. We'll buy your home in As-Is condition, make you a fair offer and pay cash and close fast with no banks, appraisers, realtors or other inconveniences involved.<br>People in the Philadelphia area say "I need to sell my house" for the following reasons:</p>

<div class="abs reason" style="left:94px;top:1448px">✓<span>Tired of bad tenants</span></div>
<div class="abs reason" style="left:94px;top:1478px">✓<span>Vacant Property</span></div>
<div class="abs reason" style="left:94px;top:1507px">✓<span>Unwanted Inheritance</span></div>
<div class="abs reason" style="left:94px;top:1537px">✓<span>Structural Damage</span></div>
<div class="abs reason" style="left:345px;top:1448px">✓<span>Job Transfer</span></div>
<div class="abs reason" style="left:345px;top:1478px">✓<span>Loss of a job</span></div>
<div class="abs reason" style="left:345px;top:1507px">✓<span>Divorce</span></div>
<div class="abs reason" style="left:345px;top:1537px">✓<span>In need of repairs</span></div>
<div class="abs reason" style="left:567px;top:1448px">✓<span>Unfavorable mortgage terms</span></div>
<div class="abs reason" style="left:567px;top:1478px">✓<span>Undesirable neighborhood</span></div>
<div class="abs reason" style="left:567px;top:1507px">✓<span>Downsizing for retirement</span></div>
<div class="abs reason" style="left:567px;top:1537px">✓<span>Looming foreclosure</span></div>
<div class="abs reason" style="left:840px;top:1446px">✓<span>Code violations with City of Philadelphia</span></div>
<div class="abs reason" style="left:840px;top:1475px">✓<span>Death of a family member</span></div>

<h2 class="abs section-title" style="top:1612px">How Our Process Works</h2>
<p class="abs body-copy" style="top:1668px">Our company is easy to work with and wont cost you anything. You're not obligated to sell for just letting us make an offer, if you wish to receive a no-hassle cash offer for your home;</p>

<div class="abs step" style="top:1708px"><span class="step-num">1</span>Call Delvane Home Buyers today at (555) 302-6614 or enter your general information on the contact form.</div>
<div class="abs step" style="top:1751px"><span class="step-num">2</span>We'll call you to get some more information about your property and figure out the best options for your situation.</div>
<div class="abs step" style="top:1796px"><span class="step-num">3</span>We can then set up a visit to your home at your convenience and arrive friendly and courteous in an unmarked vehicle.</div>
<div class="abs step" style="top:1839px"><span class="step-num">4</span>Within 48 hours we can provide you with a cash offer for your house.</div>
<div class="abs step" style="top:1882px"><span class="step-num">5</span>If the terms are acceptable you'll sign a contract, we'll open escrow with a licensed title company, and they will handle the transaction legally and professionally.</div>
<div class="abs step" style="top:1923px"><span class="step-num">6</span>At the close of escrow you pick up a check or get the funds wired into your bank account.</div>

<p class="abs body-copy" style="top:1977px;font-size:12px;line-height:26px;color:#555">So next time you hear "I need to sell my house" or wonder who the "We Buy Houses in Philadelphia" guys are, contact Delvane Home Buyers for a no-obligation cash out for your unwanted real estate.<br>Call us at (555) 302-6614 today or fill out the contact form.</p>

<footer class="abs site-footer"></footer>
<div class="abs footer-links">Terms and Conditions | Privacy Promise | FAQ's | Contact Us</div>
<div class="abs copyright">Copyright © 2013. All Rights Reserved.</div>
<div class="abs social" style="left:943px;background:#3b5aa0"></div>
<div class="abs social" style="left:983px;background:#2fa6de"></div>
<div class="abs social" style="left:1023px;background:#ee7a1e"></div>
<div class="abs social" style="left:1063px;background:#d8242a"></div>

</body>
</html>
```